"Sketch Onward Club" Social Art Website Design

I need a design for a website I am building, which will be called Sketch Onward Club. I have attached the selected logo for the site. The site will be about drawing/art, and how art can be used to brighten a stranger's day as a random act of kindness. In real life, people will receive a drawing or piece of art with details for this site on it. They will in turn be able to give a drawing or piece of art to someone else, thus building a 'chain' of people who are related to each other through the drawings they have received. This should create a strong 'social' aspect to the site. There will be areas of the site for seeing other drawings/art that have been submitted, as well as for seeing different statistics (how many drawings have been submitted, where, how people are connected, etc.).

Target Market(s)

No specific target market.

Industry/Entity Type

Building

Coding

Number of Pages Required

1 page

Font styles to use
Sans Serif
Decorative

Requirements
Must have
• Must use the logo supplied.
Nice to have
• Should be colourful and artistic. References to art tools should be primarily around drawing, though painting can also feature. Colour scheme to match the logo would be ideal.

```html
<!DOCTYPE html>
<html lang="en">
<head>
<meta charset="utf-8">
<title>Sketch Onward Club</title>
<link rel="stylesheet" href="https://fonts.googleapis.com/css2?family=Delius&family=Raleway:wght@400;500;600&display=swap">
<style>
:root{
  --pink:#ee2a7b;
  --pink-soft:#f48a8e;
  --teal:#29a8c4;
  --green:#8dc63f;
  --orange:#f5a623;
  --ink:#222;
  --text:#555;
  --muted:#777;
  --paper:#fbfbfb;
  --footer:#1f1f1f;
  --footer-text:#a9a9a9;
  --chip:#d9d9d9;
  --frame:#f2876f;
}
*{box-sizing:border-box;margin:0;padding:0}
html,body{width:1200px;height:2521px;overflow:hidden}
body{position:relative;background:var(--paper);font-family:"Raleway",sans-serif;color:var(--text)}
.abs{position:absolute}

/* soft colour washes */
.wash{position:absolute;pointer-events:none}
.wash-header{left:0;top:0;width:1200px;height:605px;
  background:
   radial-gradient(ellipse 160px 260px at 0 120px,rgba(120,200,230,.35),transparent 70%),
   radial-gradient(ellipse 150px 300px at 1200px 120px,rgba(190,150,200,.35),transparent 70%),
   radial-gradient(ellipse 160px 200px at 1200px 480px,rgba(240,160,190,.35),transparent 70%),
   radial-gradient(ellipse 180px 200px at 0 500px,rgba(140,220,200,.35),transparent 70%)}
.wash-gallery{left:0;top:932px;width:1200px;height:740px;
  background:
   radial-gradient(ellipse 150px 260px at 0 120px,rgba(245,160,150,.35),transparent 70%),
   radial-gradient(ellipse 170px 260px at 0 620px,rgba(150,215,190,.4),transparent 70%),
   radial-gradient(ellipse 150px 300px at 1200px 150px,rgba(140,210,200,.35),transparent 70%),
   radial-gradient(ellipse 160px 260px at 1200px 600px,rgba(130,190,230,.4),transparent 70%)}

/* header */
.brand{left:140px;top:26px;width:215px;display:flex;flex-direction:column;align-items:center;gap:10px}
.brand-dot{width:44px;height:44px;border-radius:50%;background:var(--teal)}
.brand-name{font-family:"Delius",cursive;font-size:24px;line-height:28px;color:#3c3c3c;white-space:nowrap}
.search{left:686px;top:15px;width:188px;height:27px;border:2px solid #9a9a9a;background:#fff;border-radius:2px;
  font-size:12px;color:#888;padding:4px 8px;font-family:"Delius",cursive}
.search svg{position:absolute;right:7px;top:5px}
.auth{top:18px;font-family:"Delius",cursive;font-size:16px;color:#222}
.nav-band{left:383px;top:62px;width:675px;height:44px;background:var(--pink-soft);border-radius:6px 14px 10px 4px;opacity:.9}
.nav{left:383px;top:62px;width:675px;height:44px;display:flex;align-items:center;list-style:none}
.nav li{position:absolute;font-family:"Delius",cursive;font-size:16px;color:#2b2b2b;white-space:nowrap}
.nav li.active{color:#fff}

/* hero */
.hero-art{left:148px;top:148px;width:914px;height:398px;border-radius:8px 20px 6px 14px;
  background:linear-gradient(100deg,#2f3a4a 0%,#b33a5a 18%,#d9923a 35%,#5a6a7a 52%,#e0b048 66%,#3a4a6a 82%,#c84a5a 100%)}
.hero-shade{left:148px;top:148px;width:914px;height:398px;border-radius:8px 20px 6px 14px;
  background:linear-gradient(180deg,rgba(20,40,60,.55) 0%,rgba(0,0,0,0) 40%,rgba(0,0,0,.15) 100%)}
.hero-title{left:193px;top:352px;font-family:"Delius",cursive;font-size:27px;line-height:37px;color:#fff;font-weight:400}
.btn{position:absolute;display:flex;align-items:center;justify-content:center;font-family:"Delius",cursive;color:#fff;border-radius:10px}
.btn-pink{background:var(--pink)}
.hero-btn{left:193px;top:442px;width:203px;height:40px;font-size:17px}
.border-band{left:0;width:1200px;height:58px;
  background:linear-gradient(180deg,rgba(255,255,255,0) 0%,#d6d6d6 40%,#9a9a9a 100%)}

/* welcome */
.section-title{left:0;width:1200px;text-align:center;font-family:"Delius",cursive;font-size:28px;color:var(--ink);font-weight:400}
.section-title .teal{color:var(--teal)}
.section-title .pink{color:var(--pink)}
.rule{height:2px;background:#bdbdbd}
.intro{left:160px;top:705px;width:882px;text-align:center;font-size:16px;line-height:28.5px;color:#666}
.btn-grey{background:var(--chip);color:#222;border-radius:8px}
.read-more{left:534px;top:840px;width:134px;height:28px;font-size:14px}

/* gallery */
.gallery-rule{left:0;width:1200px;height:3px;background:#1a1a1a}
.title-gap{background:var(--paper);padding:0 18px}
.gallery-sub{left:0;top:960px;width:1200px;text-align:center;font-size:13px;color:#666}
.card{position:absolute;width:198px}
.card-art{width:198px;height:173px;border-radius:10px 6px 12px 5px}
.card-text{margin-top:18px;font-size:12.5px;line-height:19px;color:#666;padding-left:4px;white-space:nowrap;overflow:hidden}
.card-actions{margin-top:12px;display:flex;align-items:center;gap:9px}
.chip{width:108px;height:27px;background:var(--chip);border-radius:6px;display:flex;align-items:center;justify-content:center;
  font-family:"Delius",cursive;font-size:13px;color:#222;margin-right:6px}
.view-more{left:509px;top:1651px;width:181px;height:41px;background:#111;color:var(--orange);font-size:18px;border-radius:8px}

/* stats */
.map{left:160px;top:1697px;width:880px;height:437px;border-radius:40%;
  background:radial-gradient(ellipse at center,rgba(200,200,200,.45),rgba(230,230,230,0) 70%)}
.stat{position:absolute;top:1752px;width:163px;height:118px;border:3px solid var(--frame);background:#fff;text-align:center;
  box-shadow:4px 4px 0 rgba(242,135,111,.25)}
.stat-num{margin-top:16px;font-family:"Delius",cursive;font-size:32px;line-height:36px}
.stat-label{margin-top:6px;font-size:15px;line-height:20px;color:#555}
.stat-pink .stat-num{color:var(--pink)}
.stat-teal .stat-num{color:var(--teal)}
.stat-green .stat-num{color:var(--green)}
.invite{left:0;top:1914px;width:1200px;text-align:center;font-family:"Delius",cursive;font-size:22px;line-height:30px;color:#222}
.submit-btn{left:464px;top:2004px;width:275px;height:42px;font-size:17px}

/* footer */
.footer{left:0;top:2147px;width:1200px;height:374px;background:var(--footer)}
.footer-brand{left:0;top:2168px;width:1200px;display:flex;justify-content:center;align-items:center;gap:10px}
.footer-brand .brand-dot{width:22px;height:22px;background:var(--pink)}
.footer-brand .brand-name{color:#e8e8e8;font-size:24px}
.footer-rule{height:1px;background:#4a4a4a}
.f-head{top:2230px;font-family:"Delius",cursive;font-size:19px;color:var(--orange);font-weight:400}
.f-links{left:141px;top:2275px;list-style:none}
.f-links li{font-size:13.5px;line-height:24px;color:var(--footer-text);display:flex;align-items:center;gap:14px}
.f-links li::before{content:"";width:0;height:0;border-left:6px solid #bbb;border-top:4px solid transparent;border-bottom:4px solid transparent}
.f-about{left:304px;top:2275px;width:358px;font-size:13px;line-height:22.5px;color:var(--footer-text)}
.f-read{left:304px;top:2396px;width:112px;height:24px;background:#3a3a3a;color:#ddd;font-size:12px;border-radius:6px}
.f-contact{left:700px;top:2275px;font-size:13.5px;line-height:23px;color:var(--footer-text)}
.f-contact .mail{color:var(--teal)}
.social{position:absolute;width:38px;height:38px;border-radius:50%}
.copyright{left:0;top:2481px;width:1200px;text-align:center;font-size:13px;color:#8a8a8a}
.copyright .teal{color:var(--teal)}
</style>
</head>
<body>

<div class="wash wash-header" role="img" aria-label="Soft watercolour splashes"></div>

<!-- header -->
<div class="abs brand"><span class="brand-dot"></span><span class="brand-name">Sketch Onward Club</span></div>
<div class="abs search">Find a Drawing
  <svg width="14" height="14" viewBox="0 0 14 14"><circle cx="6" cy="6" r="4" fill="none" stroke="#ee2a7b" stroke-width="2"/><line x1="9" y1="9" x2="13" y2="13" stroke="#ee2a7b" stroke-width="2"/></svg>
</div>
<div class="abs auth" style="left:900px">Sign Up</div>
<div class="abs auth" style="left:986px;display:flex;align-items:center;gap:6px">
  <svg width="11" height="14" viewBox="0 0 11 14"><rect x="1" y="6" width="9" height="7" rx="1" fill="#ee2a7b"/><path d="M3 6V4a2.5 2.5 0 0 1 5 0v2" fill="none" stroke="#ee2a7b" stroke-width="1.6"/></svg>Sign In
</div>
<div class="abs nav-band"></div>
<ul class="abs nav">
  <li class="active" style="left:48px">Home</li>
  <li style="left:136px">About Us</li>
  <li style="left:246px">Our Policies</li>
  <li style="left:377px">Report</li>
  <li style="left:470px">FAQ</li>
  <li style="left:545px">Contact Us</li>
</ul>

<!-- hero -->
<div class="abs hero-art" role="img" aria-label="Oil painting of a crowd of tall colourful figures"></div>
<div class="abs hero-shade"></div>
<h1 class="abs hero-title">Create your own art<br>to pass on to more strangers</h1>
<div class="btn btn-pink hero-btn">Drawings Submit</div>
<div class="abs border-band" style="top:550px" role="img" aria-label="Sketched wave border with stars"></div>

<!-- welcome -->
<section>
  <h2 class="abs section-title" style="top:637px">Welcome to <span class="teal">Sketch Onward Club</span></h2>
  <div class="abs rule" style="left:140px;top:690px;width:922px"></div>
  <p class="abs intro">We believe that the gift of hand-made art - a simple drawing with a nice message for a stranger – can brighten someone's day and make the world just a little bit better. We also believe everyone is an artist, whether or not you've had any training or think you have any artistic talent. We created Sketch Onward Club to join people together through art, creating an artistic chain of smiling people linked together through the simple act of drawing.</p>
  <div class="btn btn-grey read-more">Read More</div>
</section>

<!-- gallery -->
<div class="wash wash-gallery" role="img" aria-label="Soft watercolour splashes"></div>
<div class="abs gallery-rule" style="top:931px"></div>
<h2 class="abs section-title" style="top:912px"><span class="title-gap">Recently <span class="pink">Submitted Art</span></span></h2>
<p class="abs gallery-sub">Sketch Onward Club is a site about making art and giving it to strangers as a random act of kindness.</p>

<svg width="0" height="0" style="position:absolute">
  <defs>
    <symbol id="i-share" viewBox="0 0 16 16"><circle cx="12" cy="3.5" r="2" fill="none" stroke="#444" stroke-width="1.4"/><circle cx="4" cy="8" r="2" fill="none" stroke="#444" stroke-width="1.4"/><circle cx="12" cy="12.5" r="2" fill="none" stroke="#444" stroke-width="1.4"/><path d="M5.8 7 10.2 4.5M5.8 9l4.4 2.5" stroke="#444" stroke-width="1.4"/></symbol>
    <symbol id="i-like" viewBox="0 0 16 16"><path d="M2 7h3v7H2zM5 7l3-5c1.5 0 2 1 1.6 2.4L9 6.5h4.2c.9 0 1.5.8 1.3 1.6l-1.2 4.6c-.2.8-.9 1.3-1.7 1.3H5" fill="none" stroke="#444" stroke-width="1.3" stroke-linejoin="round"/></symbol>
    <symbol id="i-heart" viewBox="0 0 16 16"><path d="M8 14S1.5 9.8 1.5 5.5A3.3 3.3 0 0 1 8 4a3.3 3.3 0 0 1 6.5 1.5C14.5 9.8 8 14 8 14z" fill="none" stroke="#e0262f" stroke-width="1.5"/></symbol>
  </defs>
</svg>

<article class="card" style="left:141px;top:1010px">
  <div class="card-art" role="img" aria-label="Painted portrait artwork" style="background:linear-gradient(135deg,#e8c9a8,#a86c48 55%,#3a2a22)"></div>
  <p class="card-text">Lorem sit amet, consectetur<br>adipi scing elit. Sed vitae tellus...</p>
  <div class="card-actions"><span class="chip">View Drawing</span><svg width="16" height="16"><use href="#i-share"/></svg><svg width="16" height="16"><use href="#i-like"/></svg><svg width="16" height="16"><use href="#i-heart"/></svg></div>
</article>
<article class="card" style="left:381px;top:1010px">
  <div class="card-art" role="img" aria-label="Painting of a wave and red autumn tree" style="background:linear-gradient(120deg,#2a5a8a,#dfe6ea 45%,#d8442a 70%,#5a2a1a)"></div>
  <p class="card-text">Lorem sit amet, consectetur<br>adipi scing elit. Sed vitae tellus...</p>
  <div class="card-actions"><span class="chip">View Drawing</span><svg width="16" height="16"><use href="#i-share"/></svg><svg width="16" height="16"><use href="#i-like"/></svg><svg width="16" height="16"><use href="#i-heart"/></svg></div>
</article>
<article class="card" style="left:623px;top:1010px">
  <div class="card-art" role="img" aria-label="Pop art mosaic artwork" style="background:linear-gradient(135deg,#f2c12e,#3a7bc8 40%,#e24a3a 70%,#f2c12e)"></div>
  <p class="card-text">Lorem sit amet, consectetur<br>adipi scing elit. Sed vitae tellus...</p>
  <div class="card-actions"><span class="chip">View Drawing</span><svg width="16" height="16"><use href="#i-share"/></svg><svg width="16" height="16"><use href="#i-like"/></svg><svg width="16" height="16"><use href="#i-heart"/></svg></div>
</article>
<article class="card" style="left:864px;top:1010px">
  <div class="card-art" role="img" aria-label="Painting of red and white flowers" style="background:linear-gradient(150deg,#e8c84a,#d8322a 45%,#3a7a3a 80%,#1f3a1f)"></div>
  <p class="card-text">Lorem sit amet, consectetur<br>adipi scing elit. Sed vitae tellus...</p>
  <div class="card-actions"><span class="chip">View Drawing</span><svg width="16" height="16"><use href="#i-share"/></svg><svg width="16" height="16"><use href="#i-like"/></svg><svg width="16" height="16"><use href="#i-heart"/></svg></div>
</article>

<article class="card" style="left:141px;top:1327px">
  <div class="card-art" role="img" aria-label="Painting of a blue harbour" style="background:linear-gradient(180deg,#3a8ac8,#7ac0e0 55%,#5ac0c8)"></div>
  <p class="card-text">Lorem sit amet, consectetur<br>adipi scing elit. Sed vitae tellus...</p>
  <div class="card-actions"><span class="chip">View Drawing</span><svg width="16" height="16"><use href="#i-share"/></svg><svg width="16" height="16"><use href="#i-like"/></svg><svg width="16" height="16"><use href="#i-heart"/></svg></div>
</article>
<article class="card" style="left:381px;top:1327px">
  <div class="card-art" role="img" aria-label="Colourful painting of a horse" style="background:linear-gradient(135deg,#e87a2a,#6a3a1a 45%,#e8b04a 70%,#2a4a8a)"></div>
  <p class="card-text">Lorem sit amet, consectetur<br>adipi scing elit. Sed vitae tellus...</p>
  <div class="card-actions"><span class="chip">View Drawing</span><svg width="16" height="16"><use href="#i-share"/></svg><svg width="16" height="16"><use href="#i-like"/></svg><svg width="16" height="16"><use href="#i-heart"/></svg></div>
</article>
<article class="card" style="left:623px;top:1327px">
  <div class="card-art" role="img" aria-label="Painting of a wheat field with birds" style="background:linear-gradient(180deg,#2a3a7a,#4a6aa8 35%,#d8b02a 60%,#4a6a2a)"></div>
  <p class="card-text">Lorem sit amet, consectetur<br>adipi scing elit. Sed vitae tellus...</p>
  <div class="card-actions"><span class="chip">View Drawing</span><svg width="16" height="16"><use href="#i-share"/></svg><svg width="16" height="16"><use href="#i-like"/></svg><svg width="16" height="16"><use href="#i-heart"/></svg></div>
</article>
<article class="card" style="left:864px;top:1327px">
  <div class="card-art" role="img" aria-label="Painting of a seated figure in a yellow dress" style="background:linear-gradient(160deg,#5a7a5a,#c8a84a 50%,#e8c86a 75%,#6a5a3a)"></div>
  <p class="card-text">Lorem sit amet, consectetur<br>adipi scing elit. Sed vitae tellus...</p>
  <div class="card-actions"><span class="chip">View Drawing</span><svg width="16" height="16"><use href="#i-share"/></svg><svg width="16" height="16"><use href="#i-like"/></svg><svg width="16" height="16"><use href="#i-heart"/></svg></div>
</article>

<div class="abs gallery-rule" style="top:1670px"></div>
<div class="btn view-more">View More</div>

<!-- stats -->
<div class="abs map" role="img" aria-label="Sketched world map"></div>
<div class="stat stat-pink" style="left:232px"><div class="stat-num">250</div><div class="stat-label">Total Number<br>of Users</div></div>
<div class="stat stat-teal" style="left:519px"><div class="stat-num">1526</div><div class="stat-label">Total Drawings<br>Submitted</div></div>
<div class="stat stat-green" style="left:808px"><div class="stat-num">35</div><div class="stat-label">World With<br>Locations of Users</div></div>
<p class="abs invite">Each drawing will also be an invitation to join the site, and create your<br>own art to pass on to more strangers</p>
<div class="btn btn-pink submit-btn">Submit Your Drawings</div>
<div class="abs border-band" style="top:2092px" role="img" aria-label="Sketched wave border with stars"></div>

<!-- footer -->
<footer>
  <div class="abs footer"></div>
  <div class="abs footer-rule" style="left:141px;top:2186px;width:300px"></div>
  <div class="abs footer-rule" style="left:760px;top:2186px;width:300px"></div>
  <div class="abs footer-brand"><span class="brand-dot"></span><span class="brand-name">Sketch Onward Club</span></div>

  <h3 class="abs f-head" style="left:141px">Quick Links</h3>
  <ul class="abs f-links">
    <li>Home</li><li>About Us</li><li>Find a Drawing</li><li>Our Policies</li><li>Report</li><li>Contact Us</li>
  </ul>

  <h3 class="abs f-head" style="left:304px">About Us</h3>
  <p class="abs f-about">Sketch Onward Club is a site about making art and giving it to strangers as a random act of kindness. Each drawing will also be an invitation to join the site, and create your own art to pass on to more strangers. There is a strong social aspect to the site, on top of the artistic aspect.</p>
  <div class="btn f-read">Read More</div>

  <h3 class="abs f-head" style="left:700px">Contact us</h3>
  <div class="abs f-contact">
    <p>48 Easel Lane, Brushton,<br>United States</p>
    <p style="margin-top:10px">Phone: 010.555.0142</p>
    <p style="margin-top:5px">Email: <span class="mail">hello@sketchonward.example</span></p>
  </div>

  <h3 class="abs f-head" style="left:939px;line-height:22px">Follow<br>&nbsp;&nbsp;Us</h3>
  <svg class="abs" style="left:1008px;top:2222px" width="26" height="24" viewBox="0 0 16 16"><path d="M8 14S1.5 9.8 1.5 5.5A3.3 3.3 0 0 1 8 4a3.3 3.3 0 0 1 6.5 1.5C14.5 9.8 8 14 8 14z" fill="#e0262f"/></svg>
  <span class="social" style="left:939px;top:2272px;width:44px;height:44px;background:#3b5a9a"></span>
  <span class="social" style="left:1005px;top:2284px;background:#3aa8e0"></span>
  <span class="social" style="left:960px;top:2328px;width:34px;height:34px;background:#8a6a4a"></span>
  <span class="social" style="left:1008px;top:2338px;width:32px;height:32px;background:#d8262e"></span>
  <span class="social" style="left:983px;top:2375px;width:26px;height:26px;background:#4aa84a"></span>

  <div class="abs footer-rule" style="left:0;top:2466px;width:1200px"></div>
  <p class="abs copyright">Copyright © 2016 <span class="teal">Sketch Onward Club</span>. All Right Reserved</p>
</footer>

</body>
</html>
```